Email signature design - law firm

We are a small boutique law firm which is located near the beach in Manly, Australia.

We have just recently developed a new logo and are looking to redesign our letterhead, business cards and email signatures.

This brief is for our email signatures. This is an email signature to appear at the bottom of our Outlook emails so we would like it to be text that we are able to edit as the wording in our email signature often required amendments.

I have attached a word document which had our new logo, and our previous email signature which all the information/wording that needs to be included.

We would like multiple designs with a modern, simplistic yet striking look.

Thanks.

font - raleway or montserrat
Updates

Colors

Designer to choose colors to be used in the design.

Requirements
Must have
• Must have the exact wording which appears in the email signature in the word document attached to brief.
• Must be able to edit the text as it is for an Outlook email signature which wording will change from time to time.

```html
<!DOCTYPE html>
<html lang="en">
<head>
<meta charset="utf-8">
<title>Harlow &amp; Partners – Email Signature</title>
<link rel="stylesheet" href="https://fonts.googleapis.com/css2?family=Montserrat:wght@400;500;600;700&display=swap">
<style>
  :root {
    --page-bg: #ffffff;
    --card-bg: #ffffff;
    --card-border: #dcdcdc;
    --gold: #b49f62;
    --navy: #063f6b;
    --icon: #4f5a9e;
    --ink: #1f1f1f;
    --band-text: #ffffff;
  }
  * { box-sizing: border-box; margin: 0; padding: 0; }
  html, body {
    width: 1200px;
    height: 628px;
    overflow: hidden;
    background: var(--page-bg);
    font-family: "Montserrat", Arial, sans-serif;
    color: var(--ink);
  }
  .signature {
    position: absolute;
    left: 47px;
    top: 96px;
    width: 1106px;
    height: 436px;
    background: var(--card-bg);
    border: 1px solid var(--card-border);
  }
  .brand {
    position: absolute;
    left: 40px;
    top: 100px;
    width: 360px;
    display: flex;
    flex-direction: column;
    align-items: center;
    gap: 22px;
  }
  .brand-dot {
    width: 74px;
    height: 74px;
    border-radius: 50%;
    background: var(--icon);
  }
  .brand-name {
    font-size: 26px;
    font-weight: 600;
    letter-spacing: 1px;
    color: var(--ink);
    white-space: nowrap;
  }
  .details {
    position: absolute;
    left: 438px;
    top: 18px;
  }
  .person-name {
    font-size: 48px;
    font-weight: 600;
    color: var(--gold);
    line-height: 1.2;
    letter-spacing: 0.5px;
  }
  .designation {
    margin-top: 4px;
    font-size: 23px;
    font-weight: 600;
    color: var(--ink);
  }
  .contact-list {
    list-style: none;
    margin-top: 44px;
  }
  .contact-row {
    display: flex;
    align-items: center;
    height: 54px;
    font-size: 24px;
    font-weight: 400;
    color: var(--ink);
  }
  .contact-item {
    display: flex;
    align-items: center;
  }
  .contact-item + .contact-item { margin-left: 38px; }
  .icon {
    width: 26px;
    height: 26px;
    margin-right: 22px;
    fill: var(--icon);
    flex: none;
  }
  .firm-band {
    position: absolute;
    left: 0;
    right: 0;
    bottom: 0;
    height: 68px;
    background: var(--navy);
    display: flex;
    align-items: center;
    justify-content: center;
    color: var(--band-text);
    font-size: 31px;
    font-weight: 500;
    letter-spacing: 6px;
  }
</style>
</head>
<body>
  <section class="signature">
    <div class="brand">
      <span class="brand-dot"></span>
      <span class="brand-name">Harlow &amp; Partners</span>
    </div>

    <div class="details">
      <h1 class="person-name">Nora Whitfield</h1>
      <p class="designation">Your Designation goes here</p>

      <ul class="contact-list">
        <li class="contact-row">
          <span class="contact-item">
            <svg class="icon" viewBox="0 0 24 24" aria-hidden="true"><path d="M6.6 10.8a15.2 15.2 0 0 0 6.6 6.6l2.2-2.2a1 1 0 0 1 1-.25 11.4 11.4 0 0 0 3.6.57 1 1 0 0 1 1 1V20a1 1 0 0 1-1 1A17 17 0 0 1 3 4a1 1 0 0 1 1-1h3.5a1 1 0 0 1 1 1c0 1.25.2 2.45.57 3.57a1 1 0 0 1-.25 1z"/></svg>
            (02) 5550 1842
          </span>
          <span class="contact-item">
            <svg class="icon" viewBox="0 0 24 24" aria-hidden="true"><path d="M2 6h5v16H4a2 2 0 0 1-2-2zM9 2h9l3 3v17H9zm3 3v5h7V6.5L17.5 5zm0 8v2h2v-2zm4 0v2h2v-2zm-4 4v2h2v-2zm4 0v2h2v-2z"/></svg>
            (02) 5550 1843
          </span>
        </li>
        <li class="contact-row">
          <span class="contact-item">
            <svg class="icon" viewBox="0 0 24 24" aria-hidden="true"><path d="M12 2a10 10 0 1 0 0 20 10 10 0 0 0 0-20zm6.9 6h-2.9a15.6 15.6 0 0 0-1.4-3.6A8 8 0 0 1 18.9 8zM12 4c.8 1.2 1.5 2.5 1.9 4h-3.8c.4-1.5 1.1-2.8 1.9-4zM4.3 14a8.2 8.2 0 0 1 0-4h3.4a16.5 16.5 0 0 0 0 4zm.8 2h2.9c.3 1.3.8 2.5 1.4 3.6A8 8 0 0 1 5.1 16zM8 8H5.1a8 8 0 0 1 4.3-3.6C8.8 5.5 8.3 6.7 8 8zm4 12c-.8-1.2-1.5-2.5-1.9-4h3.8c-.4 1.5-1.1 2.8-1.9 4zm2.3-6H9.7a14.7 14.7 0 0 1 0-4h4.6a14.7 14.7 0 0 1 0 4zm.3 5.6c.6-1.1 1.1-2.3 1.4-3.6h2.9a8 8 0 0 1-4.3 3.6zM16.3 14a16.5 16.5 0 0 0 0-4h3.4a8.2 8.2 0 0 1 0 4z"/></svg>
            www.harlowandpartners.com.au
          </span>
        </li>
        <li class="contact-row">
          <span class="contact-item">
            <svg class="icon" viewBox="0 0 24 24" aria-hidden="true"><path d="M12 2a7 7 0 0 0-7 7c0 5.2 7 13 7 13s7-7.8 7-13a7 7 0 0 0-7-7zm0 9.5A2.5 2.5 0 1 1 12 6.5a2.5 2.5 0 0 1 0 5z"/></svg>
            Suite 4, 12 Coral Lane, SEAVIEW NSW 2099,
          </span>
        </li>
      </ul>
    </div>

    <footer class="firm-band">HARLOW &amp; PARTNERS</footer>
  </section>
</body>
</html>
```